Buisness card

**Front Side:**

**[Your Company Logo]**
**Steadfast Upkeep Engineering**
*Keeping Your Equipment Running Smoothly*

**Contact Information:**
- **Name:** [dale Harwick
- **Title:** [owner
- **Phone:** [5073918246
- **Email:** dale@suevx.com

**Back Side:**

**Services Offered:**
- Routine Inspections
- Equipment Maintenance
- Emergency Repairs
- Consultation Services
- New installs
Tag line
Be proactive not reactive

```html
<!DOCTYPE html>
<html lang="en">
<head>
<meta charset="utf-8">
<title>Steadfast Upkeep Engineering – Business Card</title>
<link rel="stylesheet" href="https://fonts.googleapis.com/css2?family=Jost:wght@400;500&family=Montserrat:wght@700;800&display=swap">
<style>
  :root {
    --page: #2b2c2e;
    --card-light: #ffffff;
    --card-shade: #e6e7ea;
    --navy: #1f2f6e;
    --sky: #2ea3dc;
    --ink: #3a3a3c;
    --muted: #55575c;
    --rule: #8fa3cf;
  }
  * { box-sizing: border-box; margin: 0; padding: 0; }
  html, body {
    width: 1200px; height: 900px; overflow: hidden;
    background: var(--page);
  }
  .sheet {
    width: 1200px; height: 900px;
    display: flex; flex-direction: column; align-items: center; justify-content: center;
    gap: 40px;
  }
  .card {
    position: relative;
    width: 680px; height: 388px;
    background: linear-gradient(110deg, var(--card-shade) 0%, #f1f2f4 45%, var(--card-light) 100%);
    border-radius: 3px;
    overflow: hidden;
    font-family: "Jost", sans-serif;
    color: var(--ink);
  }
  .brand {
    position: absolute; top: 38px; left: 300px;
    display: flex; align-items: center; gap: 14px;
  }
  .brand-dot {
    width: 58px; height: 58px; border-radius: 50%;
    background: var(--navy); flex: none;
  }
  .brand-text { display: flex; flex-direction: column; gap: 4px; }
  .brand-name {
    font-family: "Montserrat", sans-serif; font-weight: 800;
    font-size: 19px; color: var(--navy); letter-spacing: 0.5px; line-height: 1.1;
  }
  .brand-motto {
    font-family: "Jost", sans-serif; font-weight: 500;
    font-size: 12px; letter-spacing: 1px; color: #111; text-transform: uppercase;
  }
  /* back side */
  .services-title {
    position: absolute; left: 40px; top: 226px;
    display: flex; align-items: center; gap: 10px; width: 600px;
  }
  .services-title h2 {
    font-family: "Montserrat", sans-serif; font-weight: 800;
    font-size: 22px; color: var(--navy); white-space: nowrap;
  }
  .rule { flex: 1; height: 1px; background: var(--rule); }
  .service-list {
    position: absolute; left: 44px; top: 272px;
    list-style: none; display: grid; gap: 8px;
    font-size: 19px; color: var(--muted);
  }
  .service-list li { display: flex; gap: 10px; flex-wrap: wrap; }
  .service-list .item::before { content: "✓ "; color: var(--navy); }
  /* front side */
  .contact { position: absolute; left: 52px; top: 200px; }
  .person-name {
    font-family: "Montserrat", sans-serif; font-weight: 800;
    font-size: 22px; color: var(--navy); text-transform: uppercase;
  }
  .person-role { font-size: 18px; color: var(--muted); margin-bottom: 8px; }
  .contact-line { display: flex; align-items: center; gap: 10px; font-size: 19px; color: var(--muted); line-height: 1.45; }
  .contact-line svg { width: 20px; height: 20px; flex: none; }
  .front-rule { position: absolute; left: 52px; right: 60px; top: 320px; height: 1px; background: var(--rule); }
  .slogan {
    position: absolute; left: 52px; top: 332px;
    font-family: "Montserrat", sans-serif; font-weight: 800;
    font-size: 19px; color: var(--ink);
  }
</style>
</head>
<body>
<main class="sheet">

  <section class="card card-back">
    <div class="brand">
      <span class="brand-dot"></span>
      <div class="brand-text">
        <span class="brand-name">Steadfast Upkeep Engineering</span>
        <span class="brand-motto">Be proactive not reactive</span>
      </div>
    </div>
    <div class="services-title">
      <h2>Services Offered</h2>
      <span class="rule"></span>
    </div>
    <ul class="service-list">
      <li><span class="item">Routine Inspections</span><span class="item">Equipment Maintenance</span></li>
      <li><span class="item">Emergency Repairs</span><span class="item">Consultation Services</span><span class="item">New installs</span></li>
    </ul>
  </section>

  <section class="card card-front">
    <div class="brand">
      <span class="brand-dot"></span>
      <div class="brand-text">
        <span class="brand-name">Steadfast Upkeep Engineering</span>
        <span class="brand-motto">Be proactive not reactive</span>
      </div>
    </div>
    <div class="contact">
      <div class="person-name">dale Harwick</div>
      <div class="person-role">Owner</div>
      <div class="contact-line">
        <svg viewBox="0 0 24 24" aria-hidden="true"><path fill="#2ea3dc" d="M6.6 10.8a15.1 15.1 0 0 0 6.6 6.6l2.2-2.2a1 1 0 0 1 1-.25 11.4 11.4 0 0 0 3.6.57 1 1 0 0 1 1 1V20a1 1 0 0 1-1 1A17 17 0 0 1 3 4a1 1 0 0 1 1-1h3.5a1 1 0 0 1 1 1c0 1.25.2 2.45.57 3.57a1 1 0 0 1-.25 1z"/></svg>
        <span>5073918246</span>
      </div>
      <div class="contact-line">
        <svg viewBox="0 0 24 24" aria-hidden="true"><rect x="2" y="5" width="20" height="14" rx="1.5" fill="#2ea3dc"/><path d="M2.5 6l9.5 7 9.5-7" fill="none" stroke="#fff" stroke-width="1.6"/></svg>
        <span>dale@suevx.com</span>
      </div>
    </div>
    <span class="front-rule"></span>
    <p class="slogan">Keeping Your Equipment Running Smoothly</p>
  </section>

</main>
</body>
</html>
```